ALL TEXT GRAPHICS TM May 2025 for Instagram

We are looking for a series of social media graphics for Instagram (new size: 4:5 (1080 x 1350 pixels) ratio that are ALL TEXT. We want the following quotes below on each graphic; one quote per graphic. AND, In very small letters at the bottom of each graphic, add @TovaMarshOnline
The look and feel of these graphics should be complimentary to the color palette attached below; but keep them simple. But the design is up to you; at the end of this document, I provided various samples of all text graphics that I like as examples.
Target Market(s)
women looking to lose weight
Look and feel

```html
<!DOCTYPE html>
<html lang="en">
<head>
<meta charset="UTF-8">
<title>Tired. Moody. – Hormone Post</title>
<link rel="stylesheet" href="https://fonts.googleapis.com/css2?family=Exo+2:ital,wght@0,600;0,700;0,800;1,800&display=swap">
<style>
  :root {
    --ink: #ffffff;
    --shadow: #0d0f10;
    --window-glow: #d9a53a;
    --window-light: #c9cfc4;
    --shirt-teal: #2f6f80;
    --skin-warm: #6b4a3c;
    --hair-dark: #1c1410;
  }
  html, body {
    margin: 0;
    padding: 0;
    width: 960px;
    height: 1200px;
    overflow: hidden;
    background: var(--shadow);
  }
  .post {
    position: relative;
    width: 960px;
    height: 1200px;
    overflow: hidden;
    font-family: "Exo 2", sans-serif;
    color: var(--ink);
  }
  .post__photo {
    position: absolute;
    inset: 0;
    background:
      radial-gradient(ellipse 130px 260px at 40px 140px, var(--window-light) 0%, rgba(201,207,196,0) 100%),
      radial-gradient(ellipse 260px 200px at 200px 60px, var(--window-glow) 0%, rgba(217,165,58,0) 100%),
      radial-gradient(ellipse 240px 320px at 700px 500px, var(--skin-warm) 0%, rgba(107,74,60,0) 100%),
      radial-gradient(ellipse 320px 520px at 90px 560px, var(--shirt-teal) 0%, rgba(47,111,128,0) 100%),
      radial-gradient(ellipse 260px 300px at 900px 1150px, #24505c 0%, rgba(36,80,92,0) 100%),
      linear-gradient(160deg, #3a2e22 0%, var(--hair-dark) 45%, var(--shadow) 100%);
  }
  .headline {
    position: absolute;
    left: 96px;
    margin: 0;
    font-weight: 800;
    line-height: 1;
    letter-spacing: -1px;
  }
  .headline--tired { top: 350px; font-size: 122px; }
  .headline--moody { top: 474px; font-size: 84px; }
  .message {
    position: absolute;
    left: 0;
    width: 986px;
    margin: 0;
    text-align: center;
    font-weight: 600;
    font-size: 46px;
    line-height: 1;
    white-space: nowrap;
  }
  .message--belly { top: 675px; }
  .message--hormones { top: 752px; }
  .message--screaming { top: 820px; }
  .message--fix { top: 940px; }
  .accent { font-weight: 800; }
  .accent--fat { font-size: 66px; }
  .accent--screaming { font-size: 74px; font-style: italic; }
  .accent--fix { font-size: 76px; }
  .handle {
    position: absolute;
    left: 0;
    width: 986px;
    top: 1078px;
    margin: 0;
    text-align: center;
    font-size: 12px;
    font-weight: 700;
  }
</style>
</head>
<body>
  <main class="post">
    <div class="post__photo" role="img" aria-label="Photo of a tired woman with long brown hair resting with eyes closed by a sunlit window, wearing a teal top"></div>

    <h1 class="headline headline--tired">TIRED.</h1>
    <p class="headline headline--moody">MOODY.</p>

    <p class="message message--belly">Stubborn Belly <span class="accent accent--fat">Fat</span>.</p>
    <p class="message message--hormones">Your hormones are</p>
    <p class="message message--screaming"><span class="accent accent--screaming">screaming</span> for help!</p>
    <p class="message message--fix">Let’s <span class="accent accent--fix">fix</span> that.</p>

    <p class="handle">and@TovaMarshOnline</p>
  </main>
</body>
</html>
```